Want a DL Flyer designed for mailout, with the following info. Please see the website www.ledgerwise.com.au for any other info.
Content:
EVERYTHING YOU NEED FROM AN ACCOUNTANT
(tick) Value for money
(tick) Mobile visits to your farm or business
(tick) Fixed Fees Agreed Upfront
(tick) Advice tailored to your circumstances
(tick) Help to grow your business
(tick) Talk directly to your accountant, the person who knows you
(tick) Small business & Primary Producer Specialists
+ MORE.......LEDGERWISE. YOU'RE MORE THAN A FILE TO US.
Director: Peter Dunmore CPA | Associate: Belinda Vasey CPA
Call (07) 4619 2235 www.ledgerwise.com.au PO Box 716 Dalby Qld 4405

```html
<!DOCTYPE html>
<html lang="en">
<head>
<meta charset="utf-8">
<title>Ledgerwise DL Flyer</title>
<link href="https://fonts.googleapis.com/css2?family=Montserrat:wght@600;700&family=Roboto+Condensed:wght@400;700&family=Roboto:wght@700&family=Caveat:wght@500&display=swap" rel="stylesheet">
<style>
  :root {
    --page-bg: #eceeef;
    --paper: #ffffff;
    --teal: #14728f;
    --teal-dark: #0f5f78;
    --mist: #f1f1f3;
    --ink: #1d1d1f;
    --grey-text: #6d6f72;
    --tick-grey: #7a7c80;
    --call-grey: #a3a5a8;
    --red: #c0191f;
  }
  * { box-sizing: border-box; margin: 0; padding: 0; }
  html, body { width: 1200px; height: 1200px; overflow: hidden; background: var(--page-bg); }
  .flyer {
    position: absolute; left: 335px; top: 38px;
    width: 530px; height: 1124px;
    background: var(--paper);
    box-shadow: 0 2px 8px rgba(0,0,0,0.12);
    overflow: hidden;
  }
  .hero-photo {
    position: absolute; left: 0; top: 0; width: 530px; height: 353px;
    background: linear-gradient(135deg, #5d6670 0%, #a8b4bf 35%, #dfe6ec 65%, #c9d3dc 100%);
  }
  .hero-edge { position: absolute; left: 0; top: 320px; width: 530px; height: 34px; }
  .kicker {
    position: absolute; left: 0; top: 353px; width: 530px; height: 46px;
    background: var(--mist);
    font: 700 21.5px/46px "Montserrat", sans-serif;
    color: var(--teal); text-align: center; letter-spacing: 0.2px;
  }
  .title-band {
    position: absolute; left: 0; top: 399px; width: 530px; height: 73px;
    background: var(--teal);
    font: 700 61px/76px "Montserrat", sans-serif;
    color: #fff; text-align: center; letter-spacing: 1px;
  }
  .benefits { position: absolute; left: 40px; top: 506px; list-style: none; }
  .benefits li {
    display: flex; align-items: center; height: 35.6px;
    font: 400 16px "Roboto Condensed", sans-serif; color: var(--ink); letter-spacing: 0.3px;
  }
  .benefits svg { width: 26px; height: 26px; margin-right: 6px; flex: none; }
  .tagline {
    position: absolute; left: 0; top: 772px; width: 530px; text-align: center;
    font: 500 32px "Caveat", cursive; color: var(--teal);
  }
  .tagline-rule { position: absolute; left: 102px; top: 815px; width: 326px; height: 6px; }
  .call {
    position: absolute; left: 62px; top: 854px; height: 49px; display: flex;
    font: 700 31px/49px "Roboto", sans-serif; color: #fff;
  }
  .call-label { background: var(--call-grey); width: 147px; text-align: center; }
  .call-number { background: var(--red); width: 252px; text-align: center; }
  .team {
    position: absolute; left: 33px; top: 1002px;
    font: 400 15px/19px "Roboto Condensed", sans-serif; color: var(--grey-text);
  }
  .brand {
    position: absolute; right: 26px; top: 1010px; display: flex; align-items: center; gap: 8px;
    font: 600 26px "Montserrat", sans-serif; color: var(--red);
  }
  .brand-square { width: 14px; height: 14px; background: var(--red); }
  .footer {
    position: absolute; left: 0; top: 1075px; width: 530px; height: 49px;
    background: var(--teal); color: #fff; display: flex; align-items: center;
  }
  .footer-notch { position: absolute; left: 311px; top: 1063px; width: 30px; height: 13px; }
  .footer-address { width: 232px; text-align: center; font: 400 16px "Roboto Condensed", sans-serif; letter-spacing: 0.3px; }
  .footer-divider { width: 1.5px; height: 30px; background: #fff; }
  .footer-web { flex: 1; text-align: center; font: 700 17px "Montserrat", sans-serif; }
</style>
</head>
<body>
<main class="flyer">
  <div class="hero-photo" role="img" aria-label="Photo of an accountant's hand with a pen reviewing financial charts beside a calculator"></div>
  <svg class="hero-edge" viewBox="0 0 530 34" preserveAspectRatio="none"><polygon points="0,34 0,22 265,0 530,22 530,34" fill="#f1f1f3"/></svg>
  <h2 class="kicker">EVERYTHING YOU NEED FROM AN</h2>
  <h1 class="title-band">ACCOUNTANT</h1>
  <ul class="benefits">
    <li><svg viewBox="0 0 26 26"><circle cx="13" cy="13" r="12.5" fill="var(--tick-grey)"/><path d="M7 13.5l4 4 8-9" stroke="#fff" stroke-width="3" fill="none" stroke-linecap="round" stroke-linejoin="round"/></svg>Value for money</li>
    <li><svg viewBox="0 0 26 26"><circle cx="13" cy="13" r="12.5" fill="var(--tick-grey)"/><path d="M7 13.5l4 4 8-9" stroke="#fff" stroke-width="3" fill="none" stroke-linecap="round" stroke-linejoin="round"/></svg>Mobile visits to your farm or business</li>
    <li><svg viewBox="0 0 26 26"><circle cx="13" cy="13" r="12.5" fill="var(--tick-grey)"/><path d="M7 13.5l4 4 8-9" stroke="#fff" stroke-width="3" fill="none" stroke-linecap="round" stroke-linejoin="round"/></svg>Fixed Fees Agreed Upfront</li>
    <li><svg viewBox="0 0 26 26"><circle cx="13" cy="13" r="12.5" fill="var(--tick-grey)"/><path d="M7 13.5l4 4 8-9" stroke="#fff" stroke-width="3" fill="none" stroke-linecap="round" stroke-linejoin="round"/></svg>Advice tailored to your circumstances</li>
    <li><svg viewBox="0 0 26 26"><circle cx="13" cy="13" r="12.5" fill="var(--tick-grey)"/><path d="M7 13.5l4 4 8-9" stroke="#fff" stroke-width="3" fill="none" stroke-linecap="round" stroke-linejoin="round"/></svg>Help to grow your business</li>
    <li><svg viewBox="0 0 26 26"><circle cx="13" cy="13" r="12.5" fill="var(--tick-grey)"/><path d="M7 13.5l4 4 8-9" stroke="#fff" stroke-width="3" fill="none" stroke-linecap="round" stroke-linejoin="round"/></svg>Talk directly to your accountant, the person who knows you</li>
    <li><svg viewBox="0 0 26 26"><circle cx="13" cy="13" r="12.5" fill="var(--tick-grey)"/><path d="M7 13.5l4 4 8-9" stroke="#fff" stroke-width="3" fill="none" stroke-linecap="round" stroke-linejoin="round"/></svg>Small business &amp; Primary Producer Specialists</li>
  </ul>
  <p class="tagline">You're more than a file to us!</p>
  <svg class="tagline-rule" viewBox="0 0 326 6" preserveAspectRatio="none"><path d="M1 4 Q163 1 325 3" stroke="var(--teal)" stroke-width="2" fill="none" stroke-linecap="round"/></svg>
  <div class="call"><span class="call-label">CALL US</span><span class="call-number">(07) 4619 2235</span></div>
  <p class="team">Director: Peter Dunmore CPA<br>Associate: Belinda Vasey CPA</p>
  <div class="brand"><span class="brand-square"></span>Ledgerwise</div>
  <svg class="footer-notch" viewBox="0 0 30 13"><polygon points="0,13 15,0 30,13" fill="var(--teal)"/></svg>
  <footer class="footer">
    <span class="footer-address">PO Box 716 Dalby Qld 4405</span>
    <span class="footer-divider"></span>
    <span class="footer-web">www.ledgerwise.com.au</span>
  </footer>
</main>
</body>
</html>
```